Premium Lawn fertiliser packaging - Looking for long term designer

*Update at bottom
I need a carefully considered, bold and professional packaging design for my new premium lawn fertiliser product. This contest is for a detailed front of the stand-up pouch packaging and once I’ve chosen a winner, they’ll be asked to create the layout for the back that links to the front as well. I have a full range of additional products that will also need designs and so I'm looking for someone who can do a great job here and who we can work with long term.

The front should include our logo for Pemberly Turf Supply Direct and be titled “Bloom Vigor Max” "Professional Lawn Fertiliser". The spring fertiliser tag line is "Awaken your lawn: Lush Greening, Lasting Health".
Beneath it, it then needs to include some important usage information and the key benefits along with some suitable graphic.

Key information to include:

Apply March - June
Treats 35-50 m2
16-3-8
+2%MgO + 1% Fe + 2.9% CaO (this is the chemical makeup of the fertiliser and needs to be fairly prominent. If you look at other professional fertiliser packaging, you'll see how it needs to compare).

Key features:
Premium fertiliser, used by professionals
Advanced greening with micro-nutrient complex
Dual action Nitrogen: Instant green boost & continuous feed for 3 months
Child & pet safe

Our brand colours are purple and green. Purple = #592999, Green = 3cb64a / 81d742 / 4d9d44

I think these colours look great against a white background.

Please make sure you look at our website as well to get an idea of our brand: www.pemberlyturfsupply.co.uk

To help, I've attached images of competitors fertiliser packaging that I like the look of. I'm not looking for you to copy but just see what type of thing appeals to me, the standard I'm expecting and what I need to compete against....

In addition, I have also attached some potential images you may wish to try using in your design, although please feel free to use your own if you have something better. For the moment, the images are 'preview' images, but once I decide on a design and we agree on the correct image, I will download and send over a fully licensed version.

*** Update*** When submitting your design, can you submit it in 2 formats: The first as a fully printed custom stand-up pouch and the second as a full-size label stuck onto a standup pouch (whatever colour you think is right for your design - choose white if you are not sure). To explain, I've just discovered we won't be able to get full custom bags printed in time for the first run and so we will have to opt for the design to be printed on labels and fixed onto bags. I therefore need to choose a design that works in both formats as both a label on a standup pouch as well as a fully printed pouch. Many thanks.

Target Market(s)

Domestic home-owners

Industry/Entity Type

Lawn care. NOT AGRICULTURE OR FARMING

Font styles to use
Sans Serif

Requirements
Must have
• Presented in 2 formats - see update at bottom of description
Nice to have
• I quite like designs against a white background, although I’m open to other ideas as well.
Should not have
• Please do not include any people or faces in the design. The text should be solid in colour, so no graduated colour fill in the text or outline text. Please avoid over-busy or cluttered designs.

```html
<!DOCTYPE html>
<html lang="en">
<head>
<meta charset="utf-8">
<title>Bloom Vigor Max – Pouch Front</title>
<link rel="stylesheet" href="https://fonts.googleapis.com/css2?family=Alegreya+Sans+SC:wght@500;700;800&family=Roboto+Condensed:wght@500;700&display=swap">
<style>
  :root {
    --page-bg: #eef0ef;
    --sky-top: #f3f5f6;
    --sky-mid: #dfeef3;
    --sky-low: #b9dceb;
    --grass-light: #81d742;
    --grass-mid: #3cb64a;
    --grass-dark: #4d9d44;
    --brand-purple: #592999;
    --title-green: #4d9d44;
    --ink-brown: #3a2a1f;
    --ink-dark: #1f1f1f;
    --ink-grey: #5a6168;
    --badge-green: #2ea043;
    --white: #ffffff;
  }
  * { box-sizing: border-box; margin: 0; padding: 0; }
  html, body { width: 1200px; height: 1200px; overflow: hidden; }
  body { background: var(--page-bg); position: relative; font-family: "Alegreya Sans SC", sans-serif; }

  .pouch-front {
    position: absolute; left: 270px; top: 20px; width: 660px; height: 1160px;
    border-radius: 14px; overflow: hidden;
    background: linear-gradient(180deg, var(--sky-top) 0%, var(--sky-mid) 45%, var(--sky-low) 78%, var(--sky-mid) 100%);
  }
  .seal-band { position: absolute; left: 0; top: 0; width: 100%; height: 110px; border-bottom: 1px solid rgba(0,0,0,0.06); }

  .brand { position: absolute; top: 175px; left: 0; width: 100%; display: flex; justify-content: center; align-items: center; gap: 12px; }
  .brand-dot { width: 22px; height: 22px; border-radius: 50%; background: var(--grass-mid); }
  .brand-name { font-weight: 700; font-size: 30px; color: var(--grass-dark); letter-spacing: 1px; }

  .product-title { position: absolute; top: 250px; left: 0; width: 100%; text-align: center; font-weight: 800; color: var(--title-green); line-height: 0.95; }
  .product-title .line-1 { display: block; font-size: 112px; }
  .product-title .line-2 { display: block; font-size: 112px; }

  .product-type { position: absolute; top: 480px; left: 0; width: 100%; text-align: center; font-weight: 800; font-size: 40px; color: var(--ink-brown); }

  .usage { position: absolute; top: 535px; left: 0; width: 100%; text-align: center; color: var(--ink-dark); font-weight: 700; }
  .usage p { font-size: 25px; line-height: 1.4; }
  .usage .formula { font-size: 28px; font-family: "Roboto Condensed", sans-serif; font-weight: 500; margin-top: 2px; }

  .feature { position: absolute; width: 150px; text-align: center; font-family: "Roboto Condensed", sans-serif; color: var(--ink-grey); font-weight: 700; }
  .feature svg { display: block; margin: 0 auto 6px; }
  .feature .caption { font-size: 14px; line-height: 1.15; }
  .feature .caption small { display: block; font-size: 10px; margin-top: 3px; }
  .feature-premium { left: 30px; top: 695px; }
  .feature-greening { right: 10px; top: 675px; }
  .feature-nitrogen { left: 30px; top: 850px; }
  .feature-safe { right: 20px; top: 850px; }
  .feature-safe .caption { font-size: 20px; color: var(--ink-grey); }

  .safe-figure { width: 80px; height: 70px; margin: 0 auto 8px; border-radius: 10px; background: linear-gradient(135deg, var(--grass-light), var(--grass-mid)); }

  .scene-house { position: absolute; left: 165px; top: 690px; width: 330px; height: 330px; border-radius: 12px;
    background: linear-gradient(180deg, #c9dbe6 0%, #8e8a80 40%, #6f8a5a 75%, var(--grass-mid) 100%); }
  .lawn-base { position: absolute; left: 0; bottom: 0; width: 100%; height: 210px;
    background: linear-gradient(180deg, var(--grass-light) 0%, var(--grass-mid) 55%, var(--grass-dark) 100%); }

  .tagline { position: absolute; left: 0; width: 100%; display: flex; justify-content: center; }
  .tagline span { background: var(--brand-purple); color: var(--white); font-weight: 700; border-radius: 12px; padding: 6px 22px; box-shadow: 0 4px 8px rgba(0,0,0,0.25); }
  .tagline-1 { top: 1000px; }
  .tagline-1 span { font-size: 30px; }
  .tagline-2 { top: 1065px; }
  .tagline-2 span { font-size: 30px; }
</style>
</head>
<body>
  <main class="pouch-front">
    <div class="seal-band"></div>

    <div class="brand">
      <span class="brand-dot"></span>
      <span class="brand-name">Pemberly Turf Supply Direct</span>
    </div>

    <h1 class="product-title">
      <span class="line-1">Bloom</span>
      <span class="line-2">Vigor Max</span>
    </h1>

    <h2 class="product-type">Professional Lawn Fertiliser</h2>

    <div class="usage">
      <p>Apply March - June</p>
      <p>Treats 35-50 m2</p>
      <p class="formula">16-3-8 +2%MgO + 1% Fe + 2.9% CaO</p>
    </div>

    <div class="lawn-base" role="img" aria-label="Striped green lawn stretching to the horizon"></div>
    <div class="scene-house" role="img" aria-label="Illustration of a stone country house with a manicured garden and striped lawn"></div>

    <div class="feature feature-premium">
      <svg width="84" height="84" viewBox="0 0 84 84" aria-hidden="true">
        <circle cx="42" cy="42" r="40" fill="var(--badge-green)"/>
        <circle cx="42" cy="42" r="28" fill="var(--white)"/>
        <circle cx="42" cy="42" r="23" fill="var(--badge-green)"/>
        <path d="M31 43 L39 51 L54 34" fill="none" stroke="var(--white)" stroke-width="6" stroke-linecap="round" stroke-linejoin="round"/>
      </svg>
      <p class="caption">Premium fertiliser, used by professionals</p>
    </div>

    <div class="feature feature-greening">
      <div class="safe-figure" role="img" aria-label="Tuft of green grass"></div>
      <p class="caption">Advanced greening with micro-nutrient complex</p>
    </div>

    <div class="feature feature-nitrogen">
      <svg width="84" height="84" viewBox="0 0 84 84" aria-hidden="true">
        <path d="M42 6 A36 36 0 1 0 78 42" fill="none" stroke="var(--brand-purple)" stroke-width="6" stroke-linecap="round"/>
        <path d="M60 11 A36 36 0 0 1 76 28" fill="none" stroke="var(--brand-purple)" stroke-width="6" stroke-dasharray="3 6" stroke-linecap="round"/>
        <path d="M30 24 H54 M30 60 H54 M33 24 C33 38 51 46 51 60 M51 24 C51 38 33 46 33 60" fill="none" stroke="var(--brand-purple)" stroke-width="4" stroke-linecap="round"/>
        <path d="M36 58 L42 50 L48 58 Z" fill="var(--brand-purple)"/>
      </svg>
      <p class="caption">Dual action Nitrogen:<small>Instant green boost &amp; continuous feed for 3 months</small></p>
    </div>

    <div class="feature feature-safe">
      <div class="safe-figure" role="img" aria-label="Green icon of a child with a pet"></div>
      <p class="caption">Child &amp;<br>pet safe</p>
    </div>

    <div class="tagline tagline-1"><span>Awaken your lawn:</span></div>
    <div class="tagline tagline-2"><span>Lush Greening, Lasting Health</span></div>
  </main>
</body>
</html>
```